Mobile Oil Change company needs a flyer to promote new business

We need a flyer to 1) print & handout and 2) email out to potential customers. We are a mobile oil change company that comes to our customer locations to perform the work instead of customers going to traditional oil change companies. We have a 21 point inspection with our oil change. (21 point inspection details will not be on the flyer). Would like to keep the flyer simple but creative. I'm attaching 1) the write-up we created, 2) our logo (logo color is dark teal on white but other combinations are included if you wanted to propose a different color combination), and 3) additional services we offer. Logo font is Alegreya Sans.
Would like the additional services listed with icons and brief descriptions (similar to attachment) without pricing. Company website for reference is www.brindlefleetcare.com.

Target Market(s)

Companies with many service vehicles such as Oil & Gas service companies, heating and air conditioning companies, utility companies, police departments, etc. Companies that prioritize convenience and maintenance first.

Font styles to use
Sans Serif

Colors
00a990

Requirements
Must have
• Simple but creative design with our logo at top of the flyer. Additional Services (details in document supplied) can be smaller and less prominent than other "main" content listed in the CONTENT document supplied.
Should not have
• Do not use animated character graphics in the flyer and limit (1) stock photos to A small area in the flyer.

```html
<!DOCTYPE html>
<html lang="en">
<head>
<meta charset="utf-8">
<title>Brindle Fleet Care – Mobile Oil Change Flyer</title>
<link href="https://fonts.googleapis.com/css2?family=Arimo:wght@700&family=Source+Sans+3:ital,wght@0,600;0,700;1,400&display=swap" rel="stylesheet">
<style>
  :root{
    --teal:#00a990;
    --teal-dark:#0b6e66;
    --teal-deep:#0a4f4b;
    --red:#e8262b;
    --ink:#3a3a3a;
    --white:#ffffff;
    --photo-a:#5c6770;
    --photo-b:#c9cdd0;
  }
  *{margin:0;padding:0;box-sizing:border-box}
  html,body{width:848px;height:1200px;overflow:hidden;background:var(--white)}
  .flyer{position:relative;width:848px;height:1200px;overflow:hidden;background:var(--white);
    font-family:"Source Sans 3",Arial,sans-serif}
  .backdrop{position:absolute;inset:0}
  .headline{position:absolute;left:14px;top:72px;width:420px;text-align:center;
    font-family:"Arimo",Arial,sans-serif;font-weight:700;font-size:50px;line-height:63px;
    color:var(--red);-webkit-text-stroke:1.5px var(--white);paint-order:stroke fill;letter-spacing:-.5px}
  .brand{position:absolute;left:588px;top:42px;width:205px;height:80px;display:flex;align-items:center;justify-content:center;
    font-weight:700;font-size:27px;line-height:1;color:var(--teal-dark);text-align:center;letter-spacing:.5px}
  .intro{position:absolute;left:410px;top:362px;width:430px;font-weight:700;font-size:18.5px;line-height:24px;color:var(--red)}
  .steps{position:absolute;left:408px;top:455px;width:430px;list-style:none}
  .steps li{display:flex;align-items:flex-start;height:72px}
  .icon{flex:0 0 44px;width:44px;height:34px;margin-top:2px}
  .icon svg{width:34px;height:34px;fill:none;stroke:var(--teal-deep);stroke-width:2;stroke-linecap:round;stroke-linejoin:round}
  .steps p{font-weight:700;font-size:20px;line-height:26px;color:var(--teal);padding-left:8px}
  .section-title{position:absolute;font-family:"Arimo",Arial,sans-serif;font-weight:700;font-size:28px;color:var(--red);
    text-decoration:underline;text-decoration-thickness:2px;text-underline-offset:4px}
  .services-title{left:54px;top:484px}
  .why-title{left:456px;top:800px}
  .why{position:absolute;left:404px;top:842px;width:430px;list-style:none}
  .why li{display:flex;align-items:flex-start;margin-bottom:12px}
  .why .icon{flex:0 0 34px;width:34px;height:26px}
  .why .icon svg{width:24px;height:24px}
  .why p{font-weight:700;font-size:15.5px;line-height:22px;color:var(--teal)}
  .services{position:absolute;left:24px;top:546px;width:370px;list-style:none}
  .services li{display:flex;height:89px}
  .services .icon{flex:0 0 70px;width:70px;height:50px}
  .services .icon svg{width:48px;height:48px;stroke:var(--ink);stroke-width:1.8}
  .services h3{font-weight:700;font-size:19.5px;line-height:24px;color:var(--teal)}
  .services p{font-style:italic;font-weight:400;font-size:16px;line-height:23px;color:var(--ink)}
  .contact{position:absolute;right:24px;top:1080px;list-style:none;text-align:right}
  .contact li{display:flex;align-items:center;justify-content:flex-end;height:40px;color:var(--white);font-size:21px;font-weight:400;font-family:"Source Sans 3",Arial,sans-serif}
  .contact .badge{width:30px;height:30px;margin-left:14px;flex:0 0 30px}
  .contact .badge svg{width:30px;height:30px;fill:none;stroke:var(--white);stroke-width:1.8;stroke-linecap:round;stroke-linejoin:round}
</style>
</head>
<body>
<main class="flyer">
  <svg class="backdrop" width="848" height="1200" viewBox="0 0 848 1200" aria-hidden="false">
    <defs>
      <linearGradient id="engine" x1="0" y1="0" x2="1" y2="1">
        <stop offset="0" stop-color="var(--photo-b)"/>
        <stop offset=".5" stop-color="var(--photo-a)"/>
        <stop offset="1" stop-color="#2f3940"/>
      </linearGradient>
    </defs>
    <path role="img" aria-label="Photo of a technician checking the oil dipstick in a car engine bay"
      d="M0,0 H520 C560,150 680,260 848,300 V335 C620,335 340,360 0,470 Z" fill="url(#engine)"/>
    <path class="band-dark" d="M520,0 C560,150 680,260 848,300" fill="none" stroke="var(--teal-deep)" stroke-width="10"/>
    <path class="band-teal" d="M538,0 C580,140 690,240 848,275" fill="none" stroke="var(--teal)" stroke-width="16"/>
    <path class="band-lower" d="M848,335 C620,335 340,360 0,470" fill="none" stroke="var(--teal)" stroke-width="16"/>
    <rect class="brand-frame" x="586" y="40" width="208" height="84" rx="6" fill="var(--white)" stroke="var(--teal-dark)" stroke-width="2"/>
    <path class="foot-wave" d="M848,790 C800,990 520,1075 0,1080 V1200 H848 Z" fill="var(--teal)"/>
    <path class="foot-line" d="M848,820 C790,1010 520,1095 0,1100" fill="none" stroke="var(--white)" stroke-width="2" opacity=".6"/>
    <path class="foot-dark" d="M0,1095 C180,1110 330,1150 440,1200 H0 Z" fill="var(--teal-deep)"/>
  </svg>

  <h1 class="headline">HASSLE FREE<br>OIL CHANGES<br>ON YOUR<br>TERMS</h1>
  <div class="brand">BRINDLE<br>FLEET CARE</div>

  <p class="intro">Our simple 5-step process lets you schedule an appointment and get service to save time and money:</p>

  <ol class="steps">
    <li><span class="icon"><svg viewBox="0 0 32 32"><path d="M8 4l5 5-3 3c1 4 4 7 8 8l3-3 5 5-4 4C13 26 6 19 4 8z"/><path d="M19 6a7 7 0 0 1 7 7M19 2a11 11 0 0 1 11 11"/></svg></span><p>Call or email us to schedule service</p></li>
    <li><span class="icon"><svg viewBox="0 0 32 32"><circle cx="11" cy="12" r="4"/><path d="M11 3v3M11 18v3M2 12h3M17 12h3M5 6l2 2M15 16l2 2M5 18l2-2M15 8l2-2"/><circle cx="23" cy="23" r="3"/><path d="M23 17v2M23 27v2M17 23h2M27 23h2"/></svg></span><p>Our highly trained technicians come to you for service</p></li>
    <li><span class="icon"><svg viewBox="0 0 32 32"><circle cx="16" cy="16" r="12"/><circle cx="16" cy="16" r="9"/><path d="M20 12l-6 2-2 6 6-2z"/></svg></span><p>Service is performed quickly on your vehicle</p></li>
    <li><span class="icon"><svg viewBox="0 0 32 32"><path d="M3 20l8-6h8l4 3-4 2h-6M3 20l5 6h10l10-8"/><circle cx="24" cy="8" r="4"/></svg></span><p>Pay agreed-upon pricing and receipt is emailed to you</p></li>
    <li><span class="icon"><svg viewBox="0 0 32 32"><rect x="9" y="3" width="14" height="26" rx="2"/><path d="M14 25h4"/></svg></span><p>Services performed are tracked electronically and reminders crea</p></li>
  </ol>

  <h2 class="section-title why-title">Why Choose us</h2>
  <ul class="why">
    <li><span class="icon"><svg viewBox="0 0 24 24"><path d="M10 2C7 7 5 10 5 14a5 5 0 0 0 10 0c0-4-2-7-5-12z"/><circle cx="17" cy="19" r="3"/></svg></span><p>High quality synthetic oil used is best suited<br>for commercial vehicles</p></li>
    <li><span class="icon"><svg viewBox="0 0 24 24"><path d="M8 2l1.5 3 3 .5-2 2 .5 3L8 9l-3 1.5.5-3-2-2 3-.5zM17 12l1.5 3 3 .5-2 2 .5 3-3-1.5-3 1.5.5-3-2-2 3-.5zM5 16l1 2 2 .3-1.5 1.4.4 2L5 20.7 3.1 21.7l.4-2L2 18.3l2-.3z"/></svg></span><p>Service includes a 21-point inspection</p></li>
  </ul>

  <h2 class="section-title services-title">OUR SERVICES</h2>
  <ul class="services">
    <li><span class="icon"><svg viewBox="0 0 48 48"><rect x="6" y="8" width="36" height="32"/><rect x="10" y="12" width="28" height="24"/><path d="M14 12v24M18 12v24M22 12v24M26 12v24M30 12v24M34 12v24"/></svg></span><div><h3>Engine Air Filter Replacement</h3><p>Maintain optimum engine<br>performance.</p></div></li>
    <li><span class="icon"><svg viewBox="0 0 48 48"><path d="M8 6v36M8 10c8 0 16 4 28 0M8 18c8 0 16 4 28 0M8 26c8 0 16 4 28 0M8 34c8 0 16 4 28 0"/></svg></span><div><h3>Carbin Air Filter Replacement</h3><p>Maintain a clean A/C and fan<br>system.</p></div></li>
    <li><span class="icon"><svg viewBox="0 0 48 48"><path d="M4 16c12-8 28-8 40 0l-6 22H10z"/><path d="M24 34L14 18M12 16l-3 2M20 10l-1 3M30 10l1 3"/></svg></span><div><h3>Wiperblade Replacement</h3><p>Maintain excellent visibility on<br>the road.</p></div></li>
    <li><span class="icon"><svg viewBox="0 0 48 48"><circle cx="24" cy="24" r="18"/><circle cx="24" cy="24" r="14"/><circle cx="24" cy="26" r="4"/><path d="M10 22c5-2 23-2 28 0M22 30l-3 8M26 30l3 8"/></svg></span><div><h3>Power Steering Fluid Flush</h3><p>Maintain proper power steering<br>health.</p></div></li>
    <li><span class="icon"><svg viewBox="0 0 48 48"><rect x="8" y="6" width="22" height="36" rx="2"/><rect x="12" y="10" width="14" height="10"/><path d="M30 16l6 4v14a3 3 0 0 0 6 0V18l-4-6M4 42h30"/></svg></span><div><h3>Fuel Sysytem Treatment</h3><p>Clean your fuel system and injectors<br>to improve fuel economy.</p></div></li>
    <li><span class="icon"><svg viewBox="0 0 48 48"><circle cx="24" cy="24" r="18"/><circle cx="24" cy="24" r="6"/><circle cx="24" cy="12" r="1.5"/><circle cx="35" cy="24" r="1.5"/><circle cx="24" cy="36" r="1.5"/><circle cx="13" cy="24" r="1.5"/><path d="M30 6c8 3 12 10 12 18h-6"/></svg></span><div><h3>Brake Fluid Flush</h3><p>Maintain an excellent functioning<br>brake system.</p></div></li>
  </ul>

  <ul class="contact">
    <li>(833) 555-0148<span class="badge"><svg viewBox="0 0 30 30"><circle cx="15" cy="15" r="13"/><path d="M10 8l3 3-2 2c1 2 3 4 5 5l2-2 3 3-2 2c-6-1-10-5-11-11z"/></svg></span></li>
    <li>www.brindlefleetcare.com<span class="badge"><svg viewBox="0 0 30 30"><circle cx="15" cy="15" r="13"/><circle cx="15" cy="15" r="8"/><path d="M7 15h16M15 7c-3 3-3 13 0 16M15 7c3 3 3 13 0 16"/></svg></span></li>
    <li>Sales@BrindleFleetCare.com<span class="badge"><svg viewBox="0 0 30 30"><circle cx="15" cy="15" r="13"/><rect x="8" y="10" width="14" height="10" fill="var(--white)"/><path d="M8 10l7 5 7-5" stroke="var(--teal)"/></svg></span></li>
  </ul>
</main>
</body>
</html>
```